E-mail Ad Design Project

I would like a lower banner ad designed for placement within an e-mail. The size has to be 450px x 230px (6in x 3.07in) and must be either a GIF or JPEG, not to exceed 30K.

We are a medical billing company that provides services to physical therapy practices in Florida, and this ad is intended for owners and office managers of physical therapy businesses. We provide therapy offices with practice management software, submit medical claims on behalf of their patients, follow-up with insurance companies on outstanding claims, and also perform necessary back-end collections with patient balances. We also are able to interface with popular therapy documentation products to streamline data entry.

The design colors should incorporate our logo and red/blue colors (see www.clinicianharbor.net).

Target Market(s)

Physical therapists and administrators of physical therapy offices

Industry/Entity Type

Physical Therapy

Requirements
Must have
• Grabbing/heading text:

Tired of Denials and Confusing Rejection Codes?
We Take the Pain Out of Medical Billing.

Offer:

Get Started Today with 2 Free Months of Billing
Nice to have
• We provide services mainly to Florida therapists, so it would be nice to have an image or text that highlights this fact. Also, the e-mail campaign this is a part of will be sent to Florida recipients.

```html
<!DOCTYPE html>
<html lang="en">
<head>
<meta charset="utf-8">
<title>Clinician Harbor – Medical Billing Banner</title>
<link href="https://fonts.googleapis.com/css2?family=Roboto+Condensed:wght@400;700&display=swap" rel="stylesheet">
<style>
  :root {
    --navy: #1f2a6e;
    --red: #c8202a;
    --red-dark: #961219;
    --white: #ffffff;
    --panel-light: rgba(255,255,255,0.9);
    --panel-dark: rgba(14,18,30,0.86);
    --backdrop-a: #5aa6d8;
    --backdrop-b: #a9c9d6;
  }
  * { margin: 0; padding: 0; box-sizing: border-box; }
  html, body { width: 1200px; height: 613px; overflow: hidden; background: #fff; }
  body { font-family: "Roboto Condensed", "Arial Narrow", sans-serif; }

  .banner { position: relative; width: 1200px; height: 613px; overflow: hidden; }

  .beach-photo {
    position: absolute; inset: 0;
    background: linear-gradient(160deg, var(--backdrop-a) 0%, var(--backdrop-b) 100%);
  }

  .logo-area {
    position: absolute; left: 0; top: 0; width: 640px; height: 112px;
    background: linear-gradient(90deg, rgba(255,255,255,0.96) 62%, rgba(255,255,255,0));
  }
  .brand {
    position: absolute; left: 78px; top: 36px;
    display: flex; align-items: center; gap: 10px;
    color: var(--navy); font-weight: 700; font-size: 34px; letter-spacing: 2px;
  }
  .brand-dot { width: 24px; height: 24px; border-radius: 50%; background: var(--navy); }

  .phone {
    position: absolute; right: 44px; top: 14px;
    color: var(--white); font-weight: 700; font-size: 62px; letter-spacing: -0.5px;
    text-shadow: 0 2px 4px rgba(0,0,0,0.35);
  }

  .headline-panel {
    position: absolute; left: 0; top: 133px; width: 800px; height: 142px;
    background: var(--panel-light);
    padding: 16px 0 0 32px;
    font-weight: 700; font-size: 54px; line-height: 58px;
  }
  .txt-red { color: var(--red); }
  .txt-navy { color: var(--navy); }

  .promise-panel {
    position: absolute; left: 0; top: 275px; width: 774px; height: 178px;
    background: var(--panel-dark);
    padding: 24px 0 0 32px;
    color: var(--white); font-weight: 700; font-size: 70px; line-height: 70px;
  }

  .offer-panel {
    position: absolute; left: 0; top: 478px; width: 720px; height: 135px;
    background: var(--panel-light);
    padding: 52px 0 0 32px;
    color: var(--navy); font-weight: 700; font-size: 44px;
  }

  .offer-seal { position: absolute; left: 610px; top: 378px; width: 246px; height: 246px; }
  .seal-text {
    position: absolute; inset: 0;
    display: flex; flex-direction: column; align-items: center; justify-content: center;
    color: var(--white); font-weight: 700; font-size: 42px; line-height: 44px; text-align: center;
    transform: rotate(-15deg);
  }
</style>
</head>
<body>
<div class="banner">
  <div class="beach-photo" role="img" aria-label="Photo of a tropical beach with palm fronds, turquoise sea and two wooden lounge chairs on the sand"></div>

  <div class="logo-area">
    <div class="brand"><span>CLINICIAN</span><span class="brand-dot"></span><span>HARBOR</span></div>
  </div>

  <div class="phone">866-555-0142</div>

  <div class="headline-panel">
    <div><span class="txt-red">Tired of Denials</span><span class="txt-navy"> and</span></div>
    <div><span class="txt-red">Confusing </span><span class="txt-navy">Rejection Codes?</span></div>
  </div>

  <div class="promise-panel">
    <div>We Take the Pain Out</div>
    <div>of Medical Billing.</div>
  </div>

  <div class="offer-panel">Get Started Today with</div>

  <div class="offer-seal">
    <svg width="246" height="246" viewBox="0 0 246 246" aria-hidden="true">
      <circle cx="123" cy="123" r="121" fill="var(--red)"/>
      <circle cx="123" cy="123" r="104" fill="none" stroke="var(--red-dark)" stroke-width="3"/>
    </svg>
    <div class="seal-text"><span>2 Free</span><span>Months of</span><span>Billing</span></div>
  </div>
</div>
</body>
</html>
```